Golden Coat All-Purpose Breading Bag Design

Our client, Halvern Food Products, is looking to re-design the packaging for their product, Pellow's Golden Coat. Goldn Coat is an all-purpose food breading mix.

Halvern Foods has a registered trademark for this product, but they have not been using it for this particular 10 pound bag. They want to get the trademark onto the bag and also give the bag an updated look. They would like to continue to use the same red and blue colors. This 10 pound bag is not available on store shelves; it is sold to food service distributors who sell to restaurants.

All of the copy on the existing bag is still relevant, so we will want to incoprporate it into the bag design. Once these bags are filled with product, the tops get folded over about 1 inch and then sewn shut with thread.

Eventually, we will need the design applied to the Bag Template file attached, but that isn't important until a design is selected.

Target Market(s)

Restaurants

Industry/Entity Type

Food Manufacturing

Colors
0054AA
0677BA
7BADD7
CADEEF
E8F1F8
EB3D1F
EC4F4E
F09395
F8D3D4
FCEDEE

Requirements
Must have
• Trademark introduced to the design

```html
<!DOCTYPE html>
<html lang="en">
<head>
<meta charset="utf-8">
<title>Pellow's Golden Coat – 10 lb Bag Template</title>
<link rel="stylesheet" href="https://fonts.googleapis.com/css2?family=Open+Sans:wght@400;600;700;800&display=swap">
<style>
  :root {
    --navy: #252060;
    --red: #a51d24;
    --white: #ffffff;
    --guide: #29abe2;
    --die: #e6007e;
    --ink: #1a1a1a;
    --crumb-light: #e9a54a;
    --crumb-dark: #b8581a;
  }
  * { box-sizing: border-box; margin: 0; padding: 0; }
  html, body { width: 1200px; height: 912px; overflow: hidden; background: var(--white); }
  body { font-family: "Open Sans", Arial, sans-serif; color: var(--ink); }
  .canvas { position: relative; width: 1200px; height: 912px; overflow: hidden; }
  .artwork { position: absolute; inset: 0; }
  .abs { position: absolute; }

  .brand-name { font-weight: 800; color: var(--white); text-align: center; }
  .brand-mark { font-weight: 800; color: var(--red); line-height: 0.95; }
  .brand-maker { font-weight: 800; color: var(--navy); }

  .side-about { left: 77px; top: 470px; width: 146px; color: var(--white); font-size: 11px; line-height: 13.6px; text-align: justify; font-weight: 600; }
  .side-about p + p { margin-top: 13px; }

  .front-uses { left: 262px; top: 472px; width: 334px; text-align: center; color: var(--white); font-weight: 800; }
  .front-uses .small { font-size: 15px; line-height: 16px; }
  .front-uses .big { font-size: 34px; line-height: 32px; }
  .front-uses .note { font-size: 8.5px; line-height: 11px; font-weight: 600; }

  .food-list { left: 270px; top: 590px; width: 318px; height: 68px; background: var(--red); border-radius: 12px; color: var(--white); font-weight: 700; font-size: 12.6px; line-height: 18px; text-align: center; padding-top: 6px; }
  .label-blank { left: 388px; top: 664px; width: 82px; height: 40px; background: var(--white); }

  .directions-title { left: 626px; top: 462px; width: 158px; text-align: center; color: var(--white); font-weight: 800; font-size: 32px; line-height: 31px; }
  .directions { left: 626px; top: 547px; width: 158px; color: var(--white); font-size: 13px; line-height: 16px; text-align: justify; font-weight: 600; }

  .maker { left: 850px; top: 375px; width: 260px; text-align: center; font-size: 11px; font-weight: 700; color: var(--ink); }
  .maker .addr { font-size: 8.5px; line-height: 10px; }

  .claims { left: 808px; top: 487px; width: 344px; text-align: center; color: var(--white); }
  .claims h2 { font-size: 19px; font-weight: 700; }
  .claims .sub { font-size: 9px; font-weight: 600; line-height: 16px; }
  .claims .tagline { font-size: 16.5px; font-weight: 700; line-height: 21px; margin-top: 12px; }

  .ingredients { left: 800px; top: 627px; width: 360px; height: 93px; text-align: center; color: var(--white); padding-top: 12px; }
  .ingredients p { font-size: 9.4px; font-weight: 700; line-height: 12px; }
  .ingredients .net { font-size: 17px; font-weight: 800; margin-top: 12px; }

  .tab-copy { left: 298px; top: 738px; width: 262px; height: 132px; border: 1px solid var(--guide); display: flex; align-items: center; justify-content: center; text-align: center; color: var(--navy); font-size: 10.4px; font-weight: 700; line-height: 13.5px; }

  .spec { left: 851px; top: 784px; font-size: 15px; line-height: 20px; color: var(--ink); }

  .colorbar { left: 596px; top: 784px; font-size: 4.5px; color: var(--ink); }

  .food-photo { left: 268px; top: 304px; width: 232px; height: 166px; border-radius: 46% 54% 40% 60% / 50% 45% 55% 50%; background: radial-gradient(ellipse at 45% 45%, var(--crumb-light), var(--crumb-dark) 80%, rgba(184,88,26,0) 100%); }
</style>
</head>
<body>
<main class="canvas">
  <svg class="artwork" width="1200" height="912" viewBox="0 0 1200 912" aria-hidden="true">
    <g fill="none" stroke="var(--guide)" stroke-width="0.8" stroke-dasharray="2 2">
      <line x1="40" y1="12" x2="1160" y2="12"/>
      <line x1="50" y1="36" x2="50" y2="720"/><line x1="56" y1="36" x2="56" y2="720"/>
      <line x1="248" y1="36" x2="248" y2="720"/><line x1="256" y1="36" x2="256" y2="720"/>
      <line x1="429" y1="36" x2="429" y2="894"/><line x1="153" y1="36" x2="153" y2="720"/>
      <line x1="608" y1="36" x2="608" y2="720"/><line x1="614" y1="36" x2="614" y2="720"/>
      <line x1="796" y1="36" x2="796" y2="720"/><line x1="802" y1="36" x2="802" y2="720"/>
      <line x1="705" y1="36" x2="705" y2="720"/><line x1="980" y1="36" x2="980" y2="720"/>
      <line x1="36" y1="373" x2="1164" y2="373"/>
      <line x1="40" y1="722" x2="1160" y2="722"/>
      <polyline points="40,757 284,757 284,885 574,885 574,757 838,757 838,746 1122,746 1122,757 1160,757"/>
    </g>
    <g fill="none" stroke="var(--guide)" stroke-width="1">
      <rect x="70" y="110" width="166" height="328"/>
      <rect x="262" y="110" width="334" height="328"/>
      <rect x="622" y="110" width="166" height="328"/>
      <rect x="819" y="110" width="323" height="328"/>
    </g>
    <path d="M38,36 H1160 V758 H1110 V770 H586 V894 H272 V770 H38 Z" fill="none" stroke="var(--die)" stroke-width="1.6"/>

    <path d="M82,12 H222 V244 Q222,260 206,260 H98 Q82,260 82,244 Z" fill="var(--navy)"/>
    <path d="M634,12 H774 V244 Q774,260 758,260 H650 Q634,260 634,244 Z" fill="var(--navy)"/>

    <path d="M50,432 Q160,438 264,440 Q440,430 608,390 Q700,420 820,438 Q1000,432 1160,386 V720 H50 Z" fill="var(--navy)"/>
    <path d="M50,432 Q160,438 264,440 Q440,430 608,390 Q700,420 820,438 Q1000,432 1160,386" fill="none" stroke="var(--red)" stroke-width="4"/>
    <rect x="800" y="627" width="360" height="93" fill="var(--red)"/>
  </svg>

  <div class="abs brand-name" style="left:82px;top:210px;width:140px;font-size:17px;">Pellow's</div>
  <div class="abs brand-mark" style="left:78px;top:300px;width:150px;font-size:31px;text-align:center;">Golden<br>Coat</div>

  <div class="abs brand-maker" style="left:298px;top:118px;font-size:22px;">Pellow's</div>
  <div class="abs brand-mark" style="left:290px;top:150px;width:300px;font-size:64px;text-align:center;">Golden<br>Coat</div>

  <div class="abs brand-name" style="left:634px;top:210px;width:140px;font-size:17px;">Pellow's</div>
  <div class="abs brand-mark" style="left:630px;top:300px;width:150px;font-size:31px;text-align:center;">Golden<br>Coat</div>

  <div class="abs brand-maker" style="left:836px;top:108px;font-size:22px;">Pellow's</div>
  <div class="abs brand-mark" style="left:830px;top:140px;width:300px;font-size:68px;text-align:center;">Golden<br>Coat</div>

  <div class="abs food-photo" role="img" aria-label="Photo of crispy golden fried chicken pieces"></div>

  <div class="abs side-about">
    <p>Golden Coat is a prepared formula of pure foods that enables you to fry chicken from the raw wto the well done in ten minutes. its seals in all the a very thin crunchy coating which the fat does not penetrate - thereby using muchless fat than ordinary frying methods.</p>
    <p>This formula is an all -dry mix to be used on anything breaded - fish, oysters, shrimp, veal and chicken fried steak.</p>
  </div>

  <div class="abs front-uses">
    <div class="small">For</div>
    <div class="big">DEEP FAT</div>
    <div class="small">and</div>
    <div class="big">PAN FRYING</div>
    <div class="note">(SLIGHTLY LONGER ON PAN FRYING</div>
  </div>
  <div class="abs food-list">OF CHICKEN • STEAKS • CHOPS •TENDERLOING<br>• FISH • SHRIMP • OYSTERS &amp; OTHER SEA<br>FOODS •ONION RINGS &amp; VEGETABLES</div>
  <div class="abs label-blank"></div>

  <div class="abs directions-title">NOTING<br>TO ADD</div>
  <div class="abs directions">Wet all foods in water. then place in dry dip, coating thoroughly. Fry (350° F.) chicken 1 ½ to 2# 10 minutes, over 2# slightly longer. for best reuslts double dip onion rings and oysters.</div>

  <div class="abs maker">
    <div>By HALVERN FOOD PRODUCTS</div>
    <div class="addr">4870 ORCHARD LANE<br>CEDAR FALLS, IOWA 50613</div>
  </div>
  <div class="abs claims">
    <h2>THE ALL PURPOSE BREADING</h2>
    <div class="sub">Seals juice in - grease out</div>
    <div class="sub">Cooks two-pound chicken welldone in 10 minutes (deep fat)</div>
    <div class="tagline">Chicken fried the GOLDEN COAT way<br>is fried chicken the right way.</div>
  </div>
  <div class="abs ingredients">
    <p>INGREDIENTS: FLOUR, SALT, NON-FAT MILK SOLIDS, EGG YOLK,<br>BAKNG POWDER, CORN STRACH, SUGAR AND PEPPER.</p>
    <div class="net">NET WT. 10 LBS</div>
  </div>

  <div class="abs tab-copy">CHICKEN FRIED THE GOLDEN COAT WAY<br>IS FRIED CHICKEN THE RIGHT WAY.</div>

  <div class="abs colorbar">
    <svg width="140" height="50" viewBox="0 0 140 50">
      <rect x="0" y="2" width="8" height="8" fill="#fff200"/><rect x="33" y="2" width="8" height="8" fill="#ec008c"/>
      <rect x="66" y="2" width="8" height="8" fill="#00aeef"/><rect x="99" y="2" width="8" height="8" fill="#000"/>
      <rect x="0" y="12" width="8" height="8" fill="#000"/><rect x="33" y="12" width="8" height="8" fill="#000"/>
      <rect x="66" y="12" width="8" height="8" fill="#000"/><rect x="99" y="12" width="8" height="8" fill="#000"/>
      <rect x="0" y="22" width="8" height="8" fill="#00aeef"/><rect x="8" y="22" width="8" height="8" fill="#7fd3f5"/><rect x="16" y="22" width="8" height="8" fill="#bfe9fa"/>
      <rect x="0" y="30" width="8" height="8" fill="#fff67f"/><rect x="8" y="30" width="8" height="8" fill="#fffabf"/><rect x="16" y="30" width="8" height="8" fill="#fffde0"/>
      <rect x="40" y="22" width="8" height="8" fill="#ec008c"/><rect x="48" y="22" width="8" height="8" fill="#f57fc5"/><rect x="56" y="22" width="8" height="8" fill="#fabfe2"/>
      <rect x="40" y="30" width="8" height="8" fill="#555"/><rect x="48" y="30" width="8" height="8" fill="#999"/><rect x="56" y="30" width="8" height="8" fill="#ccc"/>
      <rect x="0" y="40" width="8" height="8" fill="#bfe9fa"/>
      <g font-family="Open Sans, sans-serif" font-size="4.5" fill="#333">
        <text x="10" y="8">Yellow</text><text x="43" y="8">Magenta</text><text x="76" y="8">Cyan</text><text x="109" y="8">Black</text>
        <text x="10" y="18">C1</text><text x="43" y="18">C2</text><text x="76" y="18">C3</text><text x="109" y="18">C4</text>
        <text x="84" y="30">A-000-000-C</text><text x="10" y="46">Varnish</text>
      </g>
    </svg>
  </div>

  <div class="abs spec">LB 7.5x4x15&nbsp; 18.5PL&nbsp; .067<br>Predistorted Flexo Template</div>
</main>
</body>
</html>
```